New Software Development Firm Needs Business Cards!

We just completed a successful logo design project on MakerHive and need to develop a business card design using that shiny new logo. We want a clean, modern design that communicates professionalism and tech savvy without being cliche'.

The company is "Bramble Logic, LLC", but our dba is "Bramble" The business card address should reflect the full company name in the address. The logo just uses "Bramble".

Photoshop or Illustrator source files will be required, along with exact font name(s) and source(s) used.

The design will need to work well with our letterhead as well. I'm also launching a project right now for letterhead and envelopes as well. Please submit to both projects! We're excited to see the designs. Thanks...

Target Market(s)

Small to medium business professionals

Industry/Entity Type

Business

Requirements
Must have
• Need place for:
- Company name and address (5 lines)
- Phone: (1 number)
- Fax: (1 number)
- Employee's name
- Employee's position
- Employee's email address
- Company web site URL
Nice to have
• Probably want a white card, but we're open to options.

```html
<!DOCTYPE html>
<html lang="en">
<head>
<meta charset="utf-8">
<title>Bramble Logic — Business Card</title>
<link rel="stylesheet" href="https://fonts.googleapis.com/css2?family=Source+Sans+3:wght@400;600&display=swap">
<style>
  :root {
    --ink: #070707;
    --paper: #ffffff;
    --canvas: #ffffff;
    --accent: #ec1c24;
    --name-grey: #555555;
    --text-grey: #5a5a5a;
    --shadow: rgba(0, 0, 0, 0.35);
  }
  html, body {
    margin: 0;
    padding: 0;
    width: 1200px;
    height: 1000px;
    overflow: hidden;
    background: var(--canvas);
    font-family: "Source Sans 3", "Myriad Pro", Arial, sans-serif;
  }
  .sheet {
    position: relative;
    width: 1200px;
    height: 1000px;
  }
  .card {
    position: absolute;
    left: 233px;
    width: 735px;
    height: 421px;
    box-shadow: 3px 5px 8px var(--shadow);
    overflow: hidden;
  }
  .card--front { top: 43px; background: var(--ink); }
  .card--back  { top: 527px; background: var(--paper); }

  .corner-flag {
    position: absolute;
    top: 0;
    right: 0;
    width: 118px;
    height: 122px;
  }
  .wordmark {
    position: absolute;
    left: 0;
    right: 0;
    text-align: center;
    font-family: "Source Sans 3", Arial, sans-serif;
    font-weight: 400;
    letter-spacing: 2px;
    line-height: 1;
  }
  .card--front .wordmark { top: 150px; font-size: 132px; color: var(--paper); }
  .card--back .wordmark  { top: 42px;  font-size: 112px; color: var(--ink); }

  .web-url {
    position: absolute;
    left: 0;
    right: 0;
    text-align: center;
    font-size: 18px;
    letter-spacing: 1.2px;
    color: var(--paper);
  }
  .card--front .web-url { top: 350px; }

  .person {
    position: absolute;
    right: calc(735px - 322px);
    top: 245px;
    text-align: right;
  }
  .person__name {
    font-size: 23px;
    font-weight: 600;
    color: var(--name-grey);
    line-height: 28px;
  }
  .person__role {
    font-size: 18px;
    color: var(--accent);
    line-height: 26px;
  }
  .divider {
    position: absolute;
    left: 366px;
    top: 191px;
    width: 2px;
    height: 164px;
    background: linear-gradient(to bottom, rgba(0,0,0,0), var(--ink) 25%, var(--ink) 75%, rgba(0,0,0,0));
  }
  .contact {
    position: absolute;
    left: 406px;
    top: 197px;
    font-size: 18px;
    line-height: 24px;
    color: var(--text-grey);
    font-style: normal;
  }
  .contact__company { color: var(--accent); }
  .contact__line { display: flex; align-items: center; white-space: nowrap; }
  .contact__line--first { margin-top: 6px; }
  .contact__icon { width: 18px; height: 16px; margin-right: 10px; flex: none; }

  .footer-tab {
    position: absolute;
    left: 0;
    bottom: 0;
    width: 735px;
    height: 50px;
  }
  .card--back .web-url { top: 382px; }
</style>
</head>
<body>
<main class="sheet">

  <section class="card card--front" aria-label="Card front">
    <svg class="corner-flag" viewBox="0 0 118 122" aria-hidden="true">
      <polygon points="0,0 118,0 118,122" fill="var(--accent)"/>
    </svg>
    <div class="wordmark">Bramble</div>
    <div class="web-url">www.bramblelogic.com</div>
  </section>

  <section class="card card--back" aria-label="Card back">
    <svg class="corner-flag" viewBox="0 0 118 122" aria-hidden="true">
      <polygon points="0,0 118,0 118,122" fill="var(--accent)"/>
    </svg>
    <div class="wordmark">Bramble</div>

    <div class="person">
      <div class="person__name">Nora Whitfield</div>
      <div class="person__role">Co Founder</div>
    </div>

    <div class="divider"></div>

    <address class="contact">
      <div class="contact__company">Bramble Logic, LLC</div>
      <div>48 Larkspur Lane, Suite 310</div>
      <div>Fairview, Oregon 97024, USA</div>
      <div class="contact__line contact__line--first">
        <svg class="contact__icon" viewBox="0 0 18 16" aria-label="Phone">
          <path d="M1 5 Q9 -1 17 5 L15 7 L12 5 L12 3.5 Q9 2.5 6 3.5 L6 5 L3 7 Z" fill="var(--accent)"/>
          <rect x="3" y="8" width="12" height="7" rx="1" fill="var(--accent)"/>
        </svg>
        (555) 214-7720
      </div>
      <div class="contact__line">
        <svg class="contact__icon" viewBox="0 0 18 16" aria-label="Fax">
          <rect x="5" y="1" width="8" height="4" fill="var(--accent)"/>
          <rect x="1" y="5" width="16" height="7" rx="1" fill="var(--accent)"/>
          <rect x="4" y="10" width="10" height="5" fill="var(--accent)" stroke="#fff" stroke-width="1"/>
        </svg>
        (555) 214-7721
      </div>
      <div class="contact__line">
        <svg class="contact__icon" viewBox="0 0 18 16" aria-label="Email">
          <rect x="1" y="3" width="16" height="11" fill="var(--accent)"/>
          <path d="M1 3 L9 10 L17 3 M1 14 L7 8.5 M17 14 L11 8.5" stroke="#fff" stroke-width="1.2" fill="none"/>
        </svg>
        nora@bramblelogic.com
      </div>
    </address>

    <svg class="footer-tab" viewBox="0 0 735 50" aria-hidden="true">
      <path d="M43 50 L58 12 Q63 0 78 0 L662 0 Q677 0 682 12 L697 50 Z" fill="var(--ink)"/>
    </svg>
    <div class="web-url">www.bramblelogic.com</div>
  </section>

</main>
</body>
</html>
```